Treatment Info-Graphic Poster

22 x 28 poster. We need a design for a poster to hang in our treatment rooms that quickly compares different treatments we offer and sets expectations for the patient. Attached is something I very quickly created on Excel, but we would like one that matches our company colors and looks much more polished. I have attached a info-graphic we have had designed prior for reference.

Target Market(s)

Osteoarthritis of the knee patients treatment comparison info graphic for poster

Font styles to use
Serif

Colors
85cae6
f78f20

Requirements
Must have
• Branded treatment comparison table
Nice to have
• Treatment graphics

```html
<!DOCTYPE html>
<html lang="en">
<head>
<meta charset="utf-8">
<title>Knee OA Treatment Comparison</title>
<link rel="stylesheet" href="https://fonts.googleapis.com/css2?family=Arvo:wght@400;700&family=Nunito+Sans:wght@400;600;700&display=swap">
<style>
:root{
  --orange:#ff7f00;
  --teal:#45d0c4;
  --dark:#333333;
  --ink:#222222;
  --header-bg:#f8f8f8;
  --body-bg:#e6fffc;
  --white:#ffffff;
}
*{box-sizing:border-box;margin:0;padding:0}
html,body{width:1200px;height:799px;overflow:hidden}
body{position:relative;background:var(--body-bg);font-family:"Nunito Sans",sans-serif;color:var(--ink)}
.masthead{position:absolute;left:0;top:0;width:1200px;height:166px;background:var(--header-bg)}
.brand-name{position:absolute;left:92px;top:52px;width:204px;text-align:center;font-family:"Arvo",serif;font-weight:700;font-size:34px;line-height:48px;color:var(--dark)}
.title{position:absolute;left:328px;top:38px;font-family:"Arvo",serif;color:var(--dark)}
.title-main{display:block;font-weight:700;font-size:42px;line-height:48px}
.title-sub{display:block;font-weight:400;font-size:32px;line-height:40px}
.tagline{position:absolute;right:67px;top:70px;font-family:"Arvo",serif;font-weight:700;font-size:17px;color:var(--orange)}
.website{position:absolute;right:72px;top:104px;font-family:"Arvo",serif;font-weight:700;font-size:13px;color:var(--ink)}

.grid{position:absolute;left:84px;display:grid;grid-template-columns:325px repeat(4,174px);column-gap:7px}
.head{top:191px}
.col-head{height:38px;display:flex;align-items:center;gap:8px;padding-left:8px;color:var(--white);font-family:"Arvo",serif;font-weight:700;font-size:9.5px}
.col-head .badge{width:26px;height:26px;border-radius:50%;background:var(--white);display:flex;align-items:center;justify-content:center;flex:none}
.col-detail{height:77px;background:var(--white);padding:5px 8px 0 8px;font-size:6.3px}
.col-detail .rule{display:flex;justify-content:flex-end;font-family:"Arvo",serif;font-weight:700;font-size:6.5px;padding-bottom:2px;border-bottom:1px solid currentColor;margin-bottom:5px}
.col-detail ul{list-style:none}
.col-detail li{display:flex;justify-content:space-between;line-height:12.8px;color:var(--ink)}
.col-detail li span:first-child::before{content:"•";margin-right:4px}
.col-detail li span:last-child{font-weight:700;width:32px}
.is-orange.col-head{background:var(--orange)}
.is-teal.col-head{background:var(--teal)}
.is-orange.col-detail .rule,.is-orange.col-detail li span:first-child::before{color:var(--orange)}
.is-teal.col-detail .rule,.is-teal.col-detail li span:first-child::before{color:var(--teal)}
.corner-top{border-top-right-radius:10px}

.body{top:307px;row-gap:6.3px}
.label{height:31px;background:var(--dark);border-radius:8px 0 0 8px;color:var(--white);font-family:"Arvo",serif;font-weight:700;font-size:11.3px;display:flex;align-items:center;justify-content:space-between;padding:0 22px 0 16px}
.label svg{flex:none}
.cell{height:31px;display:flex;align-items:center;justify-content:center}
.cell.o{background:var(--orange)}
.cell.t{background:var(--teal)}
.cell.last{border-bottom-right-radius:10px}

.disclaimer{position:absolute;left:190px;top:730px;width:934px;text-align:center;font-size:12px;line-height:15.3px;color:var(--ink)}
.paren{position:absolute;top:722px;font-size:36px;line-height:36px;color:var(--orange);font-weight:400}
.paren.left{left:178px}
.paren.right{left:1122px}
</style>
</head>
<body>
<svg width="0" height="0" style="position:absolute">
  <defs>
    <symbol id="tick" viewBox="0 0 28 22"><polyline points="3,11 11,19 25,3" fill="none" stroke="#fff" stroke-width="4.5" stroke-linecap="round" stroke-linejoin="round"/></symbol>
  </defs>
</svg>

<header class="masthead">
  <p class="brand-name">kinetiq</p>
  <h1 class="title"><span class="title-main">Knee OA</span><span class="title-sub">Treatment Comparison</span></h1>
  <p class="tagline">Portland’s Knee Pain Experts</p>
  <p class="website">www.kinetiqknees.com</p>
</header>

<section class="grid head">
  <div></div>
  <div class="col-head is-orange"><span class="badge"><svg width="14" height="14" viewBox="0 0 14 14"><line x1="2" y1="12" x2="12" y2="2" stroke="#1a7fa0" stroke-width="2.5" stroke-linecap="round"/></svg></span>Hyaluronic Acid (HA)</div>
  <div class="col-head is-teal"><span class="badge"><svg width="14" height="14" viewBox="0 0 14 14"><circle cx="5" cy="8" r="3.2" fill="#1a7fa0"/><circle cx="9.5" cy="4.5" r="2.4" fill="var(--orange)"/></svg></span>Platelet RichPlasma (PRP)</div>
  <div class="col-head is-orange"><span class="badge"><svg width="14" height="14" viewBox="0 0 14 14"><path d="M4 1 C10 4 4 10 10 13" fill="none" stroke="var(--teal)" stroke-width="2"/><path d="M10 1 C4 4 10 10 4 13" fill="none" stroke="var(--orange)" stroke-width="2"/></svg></span>Stem Cell Therapy &amp; PRP</div>
  <div class="col-head is-teal corner-top"><span class="badge"><svg width="14" height="14" viewBox="0 0 14 14"><rect x="4" y="2" width="6" height="10" rx="2" fill="var(--orange)"/></svg></span>Knee Brace(s)</div>

  <div></div>
  <div class="col-detail is-orange"><div class="rule">OA Grade</div><ul>
    <li><span>Single Injection (Visco One)</span><span>1,2,3,4</span></li>
    <li><span>Single Injection (Duravisc)</span><span>1,2,3,4</span></li>
    <li><span>3 Part Injection Series (Flexagel)</span><span>1,2,3,4</span></li>
    <li><span>3/4 Part Injection Series (Orthogel)</span><span>1,2,3,4</span></li>
  </ul></div>
  <div class="col-detail is-orange"><div class="rule">OA Grade</div><ul>
    <li><span>Single Injection (Plasmacell)</span><span>1, 2</span></li>
    <li><span>2 Part Injection Series</span><span>2, 3</span></li>
  </ul></div>
  <div class="col-detail is-orange"><div class="rule">OA Grade</div><ul>
    <li><span>Single Injection</span><span>1, 2, 3, 4</span></li>
  </ul></div>
  <div class="col-detail is-teal"><div class="rule">OA Grade</div><ul>
    <li><span>Kneeform 2</span><span>1, 2, 3, 4</span></li>
    <li><span>&nbsp;&nbsp;Patellar Stabilization</span><span>1, 2, 3, 4</span></li>
  </ul></div>
</section>

<section class="grid body">
  <div class="label">Cushion &amp; Lubricate<svg width="66" height="26" viewBox="0 0 66 26"><rect x="0" y="2" width="22" height="22" fill="var(--teal)"/><rect x="7" y="9" width="8" height="8" fill="#fff"/><path d="M28 13h9M32.5 8.5v9" stroke="#fff" stroke-width="2"/><line x1="44" y1="22" x2="60" y2="5" stroke="var(--teal)" stroke-width="4" stroke-linecap="round"/></svg></div>
  <div class="cell o"><svg width="28" height="22"><use href="#tick"/></svg></div>
  <div class="cell t"><svg width="28" height="22"><use href="#tick"/></svg></div>
  <div class="cell o"><svg width="28" height="22"><use href="#tick"/></svg></div>
  <div class="cell t"></div>

  <div class="label">Decrease Inflammation<svg width="22" height="22" viewBox="0 0 22 22"><circle cx="11" cy="11" r="10" fill="none" stroke="#fff" stroke-width="1.5"/><circle cx="11" cy="11" r="7" fill="none" stroke="var(--teal)" stroke-width="2"/><circle cx="11" cy="11" r="3.5" fill="var(--teal)"/></svg></div>
  <div class="cell o"><svg width="28" height="22"><use href="#tick"/></svg></div>
  <div class="cell t"><svg width="28" height="22"><use href="#tick"/></svg></div>
  <div class="cell o"><svg width="28" height="22"><use href="#tick"/></svg></div>
  <div class="cell t"></div>

  <div class="label">Stimulates Synovial Production of HA<svg width="24" height="24" viewBox="0 0 24 24"><rect x="2" y="10" width="5" height="12" fill="var(--teal)"/><path d="M9 10 L13 2 Q16 2 15 8 H21 Q23 9 22 12 L20 21 H9 Z" fill="var(--teal)"/></svg></div>
  <div class="cell o"><svg width="28" height="22"><use href="#tick"/></svg></div>
  <div class="cell t"><svg width="28" height="22"><use href="#tick"/></svg></div>
  <div class="cell o"><svg width="28" height="22"><use href="#tick"/></svg></div>
  <div class="cell t"></div>

  <div class="label">Healing Properties<svg width="24" height="22" viewBox="0 0 24 22"><path d="M12 21 L2 11 A5.5 5.5 0 0 1 12 4 A5.5 5.5 0 0 1 22 11 Z" fill="var(--teal)"/><path d="M12 7v7M8.5 10.5h7" stroke="#fff" stroke-width="2"/></svg></div>
  <div class="cell o"></div>
  <div class="cell t"><svg width="28" height="22"><use href="#tick"/></svg></div>
  <div class="cell o"><svg width="28" height="22"><use href="#tick"/></svg></div>
  <div class="cell t"></div>

  <div class="label">Repairative Properties<svg width="24" height="24" viewBox="0 0 24 24"><line x1="3" y1="21" x2="15" y2="9" stroke="var(--teal)" stroke-width="3.5" stroke-linecap="round"/><circle cx="17" cy="7" r="5" fill="none" stroke="var(--teal)" stroke-width="3"/></svg></div>
  <div class="cell o"></div>
  <div class="cell t"></div>
  <div class="cell o"><svg width="28" height="22"><use href="#tick"/></svg></div>
  <div class="cell t"></div>

  <div class="label">Potential Cartilage Regeneration<svg width="20" height="26" viewBox="0 0 20 26"><path d="M5 25 L7 13 L6 8 L15 2 L17 6 L11 11 L11 25 Z" fill="var(--teal)"/></svg></div>
  <div class="cell o"></div>
  <div class="cell t"></div>
  <div class="cell o"><svg width="28" height="22"><use href="#tick"/></svg></div>
  <div class="cell t"></div>

  <div class="label">On Average, Benefits Last 4-6 Months<svg width="26" height="26" viewBox="0 0 26 26"><circle cx="13" cy="13" r="12" fill="#fff"/><path d="M13 1 A12 12 0 0 1 13 25 Z" fill="var(--teal)"/></svg></div>
  <div class="cell o"><svg width="28" height="22"><use href="#tick"/></svg></div>
  <div class="cell t"><svg width="28" height="22"><use href="#tick"/></svg></div>
  <div class="cell o"><svg width="28" height="22"><use href="#tick"/></svg></div>
  <div class="cell t"><svg width="28" height="22"><use href="#tick"/></svg></div>

  <div class="label">On Average, Benefits Last 6-12 Months<svg width="26" height="26" viewBox="0 0 26 26"><circle cx="13" cy="13" r="12" fill="var(--teal)"/></svg></div>
  <div class="cell o"></div>
  <div class="cell t"><svg width="28" height="22"><use href="#tick"/></svg></div>
  <div class="cell o"><svg width="28" height="22"><use href="#tick"/></svg></div>
  <div class="cell t"><svg width="28" height="22"><use href="#tick"/></svg></div>

  <div class="label">On Average, Benefits Last 18+ Months<svg width="32" height="26" viewBox="0 0 32 26"><circle cx="13" cy="13" r="12" fill="var(--teal)"/><path d="M25 13h6M28 10v6" stroke="var(--teal)" stroke-width="1.4"/></svg></div>
  <div class="cell o"></div>
  <div class="cell t"></div>
  <div class="cell o"><svg width="28" height="22"><use href="#tick"/></svg></div>
  <div class="cell t"><svg width="28" height="22"><use href="#tick"/></svg></div>

  <div class="label">Corrects Biomechanics &amp; Stabilizes Joint<svg width="32" height="26" viewBox="0 0 32 26"><path d="M5 25 L7 13 L6 8 L15 2 L17 6 L11 11 L11 25 Z" fill="var(--teal)"/><path d="M25 13h6M28 10v6" stroke="#fff" stroke-width="1.4"/></svg></div>
  <div class="cell o"></div>
  <div class="cell t"></div>
  <div class="cell o"></div>
  <div class="cell t"><svg width="28" height="22"><use href="#tick"/></svg></div>

  <div class="label">Covered by MOST Insurance<svg width="26" height="26" viewBox="0 0 26 26"><path d="M1 13 A12 11 0 0 1 25 13 Z" fill="var(--teal)"/><path d="M13 13 V21 Q13 24 10 24 Q8 24 8 22" fill="none" stroke="var(--teal)" stroke-width="2"/></svg></div>
  <div class="cell o"><svg width="28" height="22"><use href="#tick"/></svg></div>
  <div class="cell t"></div>
  <div class="cell o"></div>
  <div class="cell t last"><svg width="28" height="22"><use href="#tick"/></svg></div>
</section>

<span class="paren left">(</span>
<p class="disclaimer">Treatment outcomes vary by individual. Treatment benefits and length of efficacy are not guaranteed. In some cases, patient’s do not respond to treatment.<br>Multiple treatments may be recommended or necessary for the best outcomes.</p>
<span class="paren right">)</span>
</body>
</html>
```